creation of business cards for Velmora Sàrl

Velmora S% 26 # 224; rl is a soci% 26 # 233; t% 26 # 233; consultancy that accompanies companies in the development of their business on the market% 26 # 233; Switzerland by providing strategic contacts or market information; and by providing administrative or logistical support. Our consulting skills focus on sectors% 26 # 224; high value added% 26 # 233; e, such as trade in food goods% 26 # 39amp; drinks, fashion% 26amp; lifestyle, products and services for% 26 # 233; s in high-tech industries (pharmaceutical, chemical, m% 26 # 233; pricy 26% 23 #; cision) or sustainable solutions (% 26 # 233; energies renewable, mat% 26 # 233; recyclable materials). As part of the launch of our activity% 26 # 233;, we need% 26 # 39;% 26 # 233; to establish business cards to d% 26 # 233; work our new customers (Swiss or international).

Target Market(s)

Companies wishing to develop their activity% 26 # 233; s in Switzerland or% 26 # 224; l% 26 # 39;% 26 # 233; abroad (mainly in Europe).

Contact Information for Business Card

Prénom NOM
Velmora Sàrl
Bureau de Lavertin
Rue des Tilleuls 14, 2000 Neuchâtel
Tél. : 032 718 46 39
info@velmora-conseil.ch
www.velmora-conseil.ch

Font styles to use
Serif
Sans Serif

Colors

Designer to choose colors to be used in the design.

Requirements
Must have
• The logo The name of the company% 26 # 233; t% 26 # 233; (Velmora S% 26 # 224; rl) One field for the mailing address One field for the number% 26 # 233; ro de t% 26 # 233; l% 26 # 233; phone One field for the % 26 # 39; email address and website

```html
<!DOCTYPE html>
<html lang="fr">
<head>
<meta charset="utf-8">
<title>Velmora Sàrl – cartes de visite</title>
<link rel="stylesheet" href="https://fonts.googleapis.com/css2?family=Open+Sans:wght@400;600;800&display=swap">
<style>
  :root {
    --maroon: #5e0a1e;
    --ink: #1c1c1c;
    --paper: #ffffff;
    --backdrop: #ecebe8;
    --card-shadow: 0 6px 18px rgba(0,0,0,.18);
  }
  * { box-sizing: border-box; margin: 0; padding: 0; }
  html, body {
    width: 1200px; height: 815px; overflow: hidden;
    background: var(--backdrop);
    font-family: "Open Sans", sans-serif;
  }
  .sheet {
    width: 1200px; height: 815px;
    display: flex; align-items: center; justify-content: center; gap: 40px;
  }
  .card {
    width: 520px; height: 336px;
    box-shadow: var(--card-shadow);
    position: relative;
  }
  /* Front side */
  .card--front { background: var(--paper); }
  .brand {
    position: absolute; left: 34px; top: 116px;
    display: flex; align-items: center; gap: 16px;
  }
  .brand__square {
    width: 46px; height: 46px; border-radius: 8px; background: var(--maroon);
  }
  .brand__name {
    font-size: 31px; font-weight: 400; letter-spacing: 3px;
    color: var(--maroon); line-height: 1;
  }
  .divider {
    position: absolute; left: 272px; top: 92px;
    width: 1.5px; height: 110px; background: var(--maroon);
  }
  .contact {
    position: absolute; left: 292px; top: 96px;
  }
  .contact__name {
    font-size: 19px; font-weight: 800; color: var(--maroon); line-height: 1.1;
  }
  .contact__company {
    font-size: 14px; color: var(--ink); margin-bottom: 10px;
  }
  .contact__line {
    display: flex; align-items: center; gap: 7px;
    font-size: 13.5px; color: var(--ink); line-height: 1.45;
  }
  .contact__line svg { width: 13px; height: 13px; flex: none; }
  .office {
    position: absolute; left: 0; right: 0; bottom: 34px; text-align: center;
  }
  .office__title { font-size: 15px; color: var(--maroon); }
  .office__address { font-size: 15px; color: var(--ink); }
  /* Back side */
  .card--back {
    background: var(--maroon);
    display: flex; align-items: center; justify-content: center; gap: 22px;
  }
  .card--back .brand__square { width: 56px; height: 56px; background: var(--paper); border-radius: 10px; }
  .card--back .brand__name { color: var(--paper); font-size: 40px; letter-spacing: 4px; }
</style>
</head>
<body>
<main class="sheet">
  <section class="card card--front" aria-label="Recto de la carte">
    <div class="brand">
      <span class="brand__square"></span>
      <span class="brand__name">VELMORA</span>
    </div>
    <span class="divider"></span>
    <div class="contact">
      <p class="contact__name">Prénom NOM</p>
      <p class="contact__company">Velmora Sàrl</p>
      <p class="contact__line">
        <svg viewBox="0 0 14 14" fill="none" stroke="#5e0a1e" stroke-width="1.2"><rect x="3.5" y="0.8" width="7" height="12.4" rx="1.2"/><line x1="6" y1="11" x2="8" y2="11"/></svg>
        +032 718 46 39
      </p>
      <p class="contact__line">
        <svg viewBox="0 0 14 14" fill="none" stroke="#5e0a1e" stroke-width="1.2"><rect x="0.8" y="3" width="12.4" height="8.5"/><polyline points="0.8,3 7,8 13.2,3"/></svg>
        info@velmora-conseil.ch
      </p>
      <p class="contact__line">
        <svg viewBox="0 0 14 14" fill="none" stroke="#5e0a1e" stroke-width="1.2"><circle cx="7" cy="7" r="6" fill="#5e0a1e"/><ellipse cx="7" cy="7" rx="2.6" ry="6" stroke="#fff" stroke-width=".8"/><line x1="1" y1="7" x2="13" y2="7" stroke="#fff" stroke-width=".8"/></svg>
        www.velmora-conseil.ch
      </p>
    </div>
    <div class="office">
      <p class="office__title">Bureau de Lavertin</p>
      <p class="office__address">Rue des Tilleuls 14, 2000 Neuchâtel</p>
    </div>
  </section>
  <section class="card card--back" aria-label="Verso de la carte">
    <span class="brand__square"></span>
    <span class="brand__name">VELMORA</span>
  </section>
</main>
</body>
</html>
```